Clean Stationary Design For Print Shop

I need a clean stationary set that properly represents a local print and copy shop to make it look amazing. It should do the following:
- Compliment the color scheme of the logo.
- Be clean and sharp.
- Be colorful but but balanced.

This is what I need designed:
- Business Card
- Letter Head
- Envelop

Target Market(s)

Local customers and businesses, including hospitals and schools.

Industry/Entity Type

Digital Printing

Requirements
Must have
• Clean business card with logo on front and full color back with faded logo on it and social icons with @hollowmeadowsco beside each one (Facebook & Instagram).

```html
<!DOCTYPE html>
<html lang="en">
<head>
<meta charset="utf-8">
<title>Hollow Meadows Stationery</title>
<link href="https://fonts.googleapis.com/css2?family=Montserrat:wght@500;600;700&family=Open+Sans:wght@400;600&display=swap" rel="stylesheet">
<style>
  :root {
    --red: #e8304a;
    --ink: #111111;
    --paper: #ffffff;
    --backdrop: #ebeae8;
    --grey: #555555;
    --faint: #f6e4e7;
  }
  * { box-sizing: border-box; margin: 0; padding: 0; }
  html, body { width: 1200px; height: 2540px; overflow: hidden; }
  body { background: var(--backdrop); font-family: "Open Sans", sans-serif; color: var(--ink); position: relative; }

  .sheet { position: absolute; background: var(--paper); box-shadow: 0 4px 14px rgba(0,0,0,.12); overflow: hidden; }

  .brand { display: flex; align-items: center; gap: 10px; position: relative; z-index: 2; }
  .brand-mark { background: var(--red); flex: none; }
  .brand-name { font-family: "Montserrat", sans-serif; font-weight: 600; color: var(--ink); line-height: 1; white-space: nowrap; }
  .brand-tag { font-family: "Montserrat", sans-serif; font-weight: 700; letter-spacing: .06em; color: var(--grey); text-transform: uppercase; white-space: nowrap; }
  .on-dark .brand-name { color: var(--paper); }
  .on-dark .brand-tag { color: #cfcfcf; }

  .edge { position: absolute; left: 0; right: 0; bottom: 0; height: 22px; z-index: 2; }
  .edge-red { position: absolute; left: 0; bottom: 0; height: 12px; background: var(--red); }
  .edge-black { position: absolute; right: 0; bottom: 6px; height: 10px; background: var(--ink); }

  /* business cards */
  .card-back { left: 60px; top: 80px; width: 520px; height: 297px; background: var(--ink); }
  .card-back .brand { position: absolute; left: 110px; top: 100px; }
  .card-back .brand-mark { width: 40px; height: 40px; }
  .card-back .brand-name { font-size: 34px; }
  .card-back .brand-tag { font-size: 9.5px; margin-top: 4px; }
  .social { position: absolute; left: 190px; top: 212px; display: flex; align-items: center; gap: 6px; color: #dcdcdc; font-size: 12px; }
  .social-dot { width: 12px; height: 12px; border-radius: 50%; background: var(--red); }

  .card-front { left: 620px; top: 80px; width: 520px; height: 297px; }
  .card-front .brand { position: absolute; left: 110px; top: 54px; }
  .card-front .brand-mark { width: 40px; height: 40px; }
  .card-front .brand-name { font-size: 34px; }
  .card-front .brand-tag { font-size: 9.5px; margin-top: 4px; }
  .person { position: absolute; left: 44px; top: 160px; }
  .person-name { font-family: "Montserrat", sans-serif; font-weight: 700; font-size: 15px; text-transform: uppercase; }
  .person-role { font-family: "Montserrat", sans-serif; font-weight: 600; font-size: 14px; color: var(--red); }
  .divider { position: absolute; left: 250px; top: 140px; width: 1px; height: 90px; background: #999; }
  .contact { position: absolute; left: 266px; top: 138px; font-size: 12px; line-height: 1.55; list-style: none; }
  .contact li { display: flex; align-items: center; gap: 6px; }
  .contact svg { flex: none; }
  .card-front .edge-red { width: 110px; }
  .card-front .edge-black { left: 116px; }

  /* letterhead */
  .letterhead { left: 110px; top: 480px; width: 620px; height: 877px; }
  .letterhead .brand { position: absolute; left: 48px; top: 46px; gap: 7px; }
  .letterhead .brand-mark { width: 20px; height: 20px; }
  .letterhead .brand-name { font-size: 17px; }
  .letterhead .brand-tag { font-size: 5px; margin-top: 2px; }
  .letter-watermark { position: absolute; left: 200px; top: 520px; width: 220px; height: 240px; background: var(--faint); opacity: .7; }
  .letter-contact { position: absolute; right: 46px; top: 110px; font-size: 7px; line-height: 1.5; list-style: none; }
  .letter-contact li { display: flex; align-items: center; gap: 4px; }
  .letter-body { position: absolute; left: 48px; top: 150px; width: 400px; font-size: 8.5px; line-height: 1.65; color: #333; z-index: 1; }
  .letter-body p { margin-bottom: 12px; }
  .signature { width: 60px; height: 30px; background: #e4e4e4; margin-top: 6px; }
  .letterhead .edge-red { width: 70px; bottom: 40px; height: 8px; }
  .letterhead .edge-black { left: 76px; bottom: 34px; height: 7px; }

  /* vertical cards */
  .vcard { width: 180px; height: 316px; }
  .vcard-light { left: 850px; top: 560px; }
  .vcard-dark { left: 850px; top: 920px; background: var(--ink); }
  .vcard .brand-mark { position: absolute; left: 55px; top: 110px; width: 70px; height: 70px; }
  .vcard-web { position: absolute; left: 0; right: 0; bottom: 30px; text-align: center; font-size: 7px; color: #555; }

  /* envelopes */
  .env-back { left: 120px; top: 1450px; width: 960px; height: 420px; }
  .env-flap { position: absolute; left: 0; right: 0; top: 0; height: 110px; background: var(--ink); }
  .env-flap .brand { position: absolute; right: 260px; top: 36px; }
  .env-flap .brand-mark { width: 26px; height: 26px; }
  .env-flap .brand-name { font-size: 24px; }
  .env-flap .brand-tag { font-size: 7px; margin-top: 3px; }

  .env-front { left: 120px; top: 1930px; width: 960px; height: 450px; }
  .env-front .brand { position: absolute; left: 50px; top: 44px; }
  .env-front .brand-mark { width: 26px; height: 26px; }
  .env-front .brand-name { font-size: 24px; }
  .env-front .brand-tag { font-size: 7px; margin-top: 3px; }
  .env-return { position: absolute; left: 86px; top: 90px; font-size: 10px; line-height: 1.5; color: #444; }
  .env-watermark { position: absolute; right: 160px; top: 150px; width: 240px; height: 300px; background: var(--faint); z-index: 0; }
  .env-front .edge-red { width: 110px; bottom: 90px; height: 12px; }
  .env-front .edge-black { left: 116px; bottom: 84px; height: 10px; }
</style>
</head>
<body>

<section class="sheet card-back on-dark" aria-label="Business card back">
  <div class="brand">
    <span class="brand-mark"></span>
    <div>
      <div class="brand-name">Hollow Meadows</div>
      <div class="brand-tag">Sharp Prints, Fast Turnaround</div>
    </div>
  </div>
  <div class="social">
    <span class="social-dot"></span><span class="social-dot"></span>
    <span>@hollowmeadowsco</span>
  </div>
</section>

<section class="sheet card-front" aria-label="Business card front">
  <div class="brand">
    <span class="brand-mark"></span>
    <div>
      <div class="brand-name">Hollow Meadows</div>
      <div class="brand-tag">Sharp Prints, Fast Turnaround</div>
    </div>
  </div>
  <div class="person">
    <div class="person-name">Dana Whitfield</div>
    <div class="person-role">Managing Director</div>
  </div>
  <div class="divider"></div>
  <ul class="contact">
    <li>1420 Larkspur Lane</li>
    <li>Fairbrook, OH 45100</li>
    <li><svg width="11" height="11" viewBox="0 0 12 12"><path d="M3 1l2 2-1 2a7 7 0 003 3l2-1 2 2-1 2C5 11 1 7 1 2z" fill="#e8304a"/></svg>555 014 2290</li>
    <li><svg width="11" height="11" viewBox="0 0 12 12"><rect x="1" y="3" width="10" height="7" fill="#e8304a"/><path d="M1 3l5 4 5-4" stroke="#fff" fill="none"/></svg>dana@hollowmeadowsco.com</li>
    <li><svg width="11" height="11" viewBox="0 0 12 12"><circle cx="6" cy="6" r="5" fill="#e8304a"/></svg>www.hollowmeadowsco.com</li>
  </ul>
  <div class="edge"><span class="edge-red"></span><span class="edge-black"></span></div>
</section>

<section class="sheet letterhead" aria-label="Letterhead">
  <div class="letter-watermark"></div>
  <div class="brand">
    <span class="brand-mark"></span>
    <div>
      <div class="brand-name">Hollow Meadows</div>
      <div class="brand-tag">Sharp Prints, Fast Turnaround</div>
    </div>
  </div>
  <ul class="letter-contact">
    <li>1420 Larkspur Lane</li>
    <li>Fairbrook, OH 45100</li>
    <li><svg width="7" height="7" viewBox="0 0 12 12"><rect width="12" height="12" fill="#e8304a"/></svg>555 014 2290</li>
    <li><svg width="7" height="7" viewBox="0 0 12 12"><rect width="12" height="12" fill="#e8304a"/></svg>dana@hollowmeadowsco.com</li>
    <li><svg width="7" height="7" viewBox="0 0 12 12"><circle cx="6" cy="6" r="6" fill="#e8304a"/></svg>www.hollowmeadowsco.com</li>
  </ul>
  <div class="letter-body">
    <p>Dear customer,</p>
    <p>Thank you for choosing our shop for your recent print order. We take pride in sharp colour, clean finishing and fast turnaround on every job, large or small, for homes, schools and local businesses.</p>
    <p>Our team reviews each file before it goes to press, so your cards, letterheads and envelopes arrive exactly as planned. If anything needs a change, we will call you before a single sheet is printed.</p>
    <p>We also offer wide format posters, banners and signage for hospitals, schools and events. Ask about our volume pricing and same day service for urgent orders placed before noon.</p>
    <p>We look forward to working with you again soon and helping your next project look its very best.</p>
    <p>Yours Sincerely,</p>
    <div class="signature" role="img" aria-label="Handwritten signature"></div>
  </div>
  <div class="edge"><span class="edge-red"></span><span class="edge-black"></span></div>
</section>

<section class="sheet vcard vcard-light" aria-label="Vertical card light">
  <span class="brand-mark"></span>
  <div class="vcard-web">www.hollowmeadowsco.com</div>
</section>
<section class="sheet vcard vcard-dark" aria-label="Vertical card dark">
  <span class="brand-mark"></span>
</section>

<section class="sheet env-back" aria-label="Envelope back">
  <div class="env-flap on-dark">
    <div class="brand">
      <span class="brand-mark"></span>
      <div>
        <div class="brand-name">Hollow Meadows</div>
        <div class="brand-tag">Sharp Prints, Fast Turnaround</div>
      </div>
    </div>
  </div>
</section>

<section class="sheet env-front" aria-label="Envelope front">
  <div class="env-watermark"></div>
  <div class="brand">
    <span class="brand-mark"></span>
    <div>
      <div class="brand-name">Hollow Meadows</div>
      <div class="brand-tag">Sharp Prints, Fast Turnaround</div>
    </div>
  </div>
  <div class="env-return">1420 Larkspur Lane<br>Fairbrook, OH 45100</div>
  <div class="edge"><span class="edge-red"></span><span class="edge-black"></span></div>
</section>

</body>
</html>
```